Law Firm Business Card

This is a business card for a law firm that serves US military and veterans.

The card must have ONLY the following (we want an uncluttered look):

- Company logo (PNG, GIF, JPEG copies uploaded)
- A tagline reading: "a law firm for service members and veterans"
- My name and title: "Martin Kovel" and "Attorney"
- My email: "mart.kovel@bramblecourtlegal.com"
- My number: "855-MOKE-TIB (665-3842)"

We are looking for a clean, simple layout with only the above information, likely printed on a bright white cotton stock. The font of our logo is DIN 1451, and the font used on our website is Helvetica Neue. The color of our logo is #336699, and we probably want the tagline in that color also, and my contact information in a dark grey. Please review our website at www.bramblecourtlegal.com to ensure your card design complements our website style.

Thanks and we look forward to seeing your submissions.

A few notes:

- Two-sided submissions are ok
- Please don't add graphics (scales of justice, judges hammer, etc)

```html
<!DOCTYPE html>
<html lang="en">
<head>
<meta charset="UTF-8">
<title>Bramble Court Legal — Business Card</title>
<link href="https://fonts.googleapis.com/css2?family=Inter:wght@300;400;600&display=swap" rel="stylesheet">
<style>
  :root {
    --brand-blue: #336699;
    --ink-grey: #555a5e;
    --card-white: #ffffff;
    --backdrop: #c9c9c9;
  }
  * { margin: 0; padding: 0; box-sizing: border-box; }
  html, body {
    width: 1200px;
    height: 720px;
    overflow: hidden;
    background: var(--backdrop);
    font-family: "Inter", "Helvetica Neue", Arial, sans-serif;
  }
  .card {
    position: absolute;
    left: 75px;
    top: 60px;
    width: 1050px;
    height: 600px;
    background: var(--card-white);
    box-shadow: 0 6px 24px rgba(0, 0, 0, 0.18);
  }
  .brand {
    position: absolute;
    top: 110px;
    left: 0;
    width: 100%;
    display: flex;
    justify-content: center;
    align-items: center;
    gap: 22px;
  }
  .brand-dot {
    width: 34px;
    height: 34px;
    border-radius: 50%;
    background: var(--brand-blue);
  }
  .brand-name {
    font-weight: 600;
    font-size: 64px;
    letter-spacing: 1px;
    color: var(--brand-blue);
    text-transform: uppercase;
  }
  .tagline {
    position: absolute;
    top: 228px;
    width: 100%;
    text-align: center;
    font-weight: 400;
    font-size: 27px;
    color: var(--brand-blue);
  }
  .person {
    position: absolute;
    top: 300px;
    width: 100%;
    text-align: center;
    color: var(--ink-grey);
  }
  .person-name {
    font-weight: 300;
    font-size: 42px;
    line-height: 1.1;
  }
  .person-title {
    font-weight: 300;
    font-size: 26px;
    margin-top: 4px;
  }
  .contact {
    position: absolute;
    bottom: 48px;
    left: 50px;
    right: 50px;
    display: flex;
    justify-content: space-between;
    align-items: center;
  }
  .contact-item {
    display: flex;
    align-items: center;
    gap: 16px;
    font-weight: 300;
    font-size: 24px;
    color: var(--ink-grey);
  }
  .contact-icon { width: 34px; height: 34px; flex: none; }
</style>
</head>
<body>
  <div class="card">
    <div class="brand">
      <span class="brand-dot"></span>
      <span class="brand-name">Bramble Court Legal</span>
    </div>

    <p class="tagline">a law firm for service members and veterans</p>

    <div class="person">
      <p class="person-name">Martin Kovel</p>
      <p class="person-title">Attorney</p>
    </div>

    <div class="contact">
      <div class="contact-item">
        <svg class="contact-icon" viewBox="0 0 34 34" aria-hidden="true">
          <circle cx="17" cy="17" r="17" fill="#336699"/>
          <path d="M11.5 9.5c1-.6 2-.4 2.6.5l1.6 2.5c.5.8.3 1.7-.4 2.3l-1 .8c.8 1.8 2.2 3.3 4 4.2l.9-1c.6-.7 1.6-.8 2.3-.3l2.4 1.7c.8.6 1 1.7.4 2.6l-.8 1.1c-.7 1-2 1.4-3.2 1-4.8-1.6-8.4-5.3-9.9-10.1-.4-1.2.1-2.5 1.1-3.3z" fill="#fff"/>
        </svg>
        <span>855-MOKE-TIB (665-3842)</span>
      </div>
      <div class="contact-item">
        <svg class="contact-icon" viewBox="0 0 34 34" aria-hidden="true">
          <circle cx="17" cy="17" r="17" fill="#336699"/>
          <rect x="8.5" y="11" width="17" height="12" rx="1.2" fill="#fff"/>
          <path d="M9 11.8l8 6.2 8-6.2" fill="none" stroke="#336699" stroke-width="1.5"/>
        </svg>
        <span>mart.kovel@bramblecourtlegal.com</span>
      </div>
    </div>
  </div>
</body>
</html>
```